Einladungskarten-Design für Reinigung & Gebäudemangement
Zielgruppe:
Potentielle Kunden/Entscheider Einrichtungsleiter, Geschäftführer für den Bereich Alten- und Pflegeheime, Krankenhäuser.
Das Angebot geht über Verpflegungslösung, Reinigung, Gebäudemangement und Innovationen (z.B. zum Thema Digitalisierung, Roboting, .....).
Der Claim des Unternehmens ist 'Quality of Life Services = DIENSTE FÜR MEHR WOHLGEFÜHL'
Aufgabenstellung
Gerne Pop-Up oder auch Relief - hochwertige Haptik von Umschlag und Karte ggf. Sonderformat d.h. nicht Standard DL quer
Sollte aber dennoch klassich gut wirken.
Die persönliche Note erhält die Karte durch handschriftliche Personalisierung durch den Sales Mitarbeiter.
Die Karte soll folgenden Text enthalten.
Text:
Das neue Jahr liegt vor Ihnen.
Nutzen Sie seine Chancen und ergreifen Sie seine Möglichkeiten.
Beispielsweise mit einem Gespräch
über inspierierende Ideen und neue Konzepte zur Steigerung der Lebensqualität
in Ihrem Hause.
Wir freuen uns mit Ihnen in Kontakt zu sein.
Der Umschlag soll Absenderadresse und Logo enthalten - dies wird nach Prämierung bekannt gegeben.
Natürlich kann auf der Rückseite der Karte auch das Logo mit Claim aufgedruckt werden.
Alle Bildrechte sollen nach Prämierung auf den Auftraggeber übergehen.

```html
<!DOCTYPE html>
<html lang="de">
<head>
<meta charset="utf-8">
<title>Neujahrskarte – Das neue Jahr liegt vor Ihnen</title>
<link href="https://fonts.googleapis.com/css2?family=Lato:wght@300;400;700;900&display=swap" rel="stylesheet">
<style>
  :root {
    --paper: #ffffff;
    --ink: #1d1d1b;
    --headline: #ffffff;
    --year-stroke: #6f7f95;
    --sky-top: #7d6148;
    --sky-mid: #c98a3c;
    --sky-glow: #e8932a;
    --rock: #1f1510;
  }
  * { margin: 0; padding: 0; box-sizing: border-box; }
  html, body { width: 800px; height: 1200px; overflow: hidden; background: var(--paper); }
  .card {
    position: relative;
    width: 800px;
    height: 1200px;
    background: var(--paper);
    font-family: 'Lato', sans-serif;
  }
  .brand {
    position: absolute;
    left: 0;
    right: 0;
    top: 54px;
    display: flex;
    flex-direction: column;
    align-items: center;
    transform: rotate(180deg);
    color: var(--ink);
  }
  .brand-name {
    display: flex;
    align-items: center;
    gap: 6px;
    font-size: 24px;
    font-weight: 700;
    letter-spacing: 0.5px;
    line-height: 1;
  }
  .brand-dot {
    width: 7px;
    height: 7px;
    border-radius: 50%;
    background: var(--ink);
  }
  .brand-claim {
    margin-top: 6px;
    font-size: 9.5px;
    font-weight: 900;
    letter-spacing: 0.9px;
    line-height: 1;
  }
  .hero {
    position: absolute;
    left: 0;
    top: 601px;
    width: 800px;
    height: 599px;
    overflow: hidden;
  }
  .hero-photo {
    position: absolute;
    inset: 0;
    background:
      linear-gradient(180deg, rgba(31,21,16,0) 0%, rgba(31,21,16,0) 78%, var(--rock) 100%),
      radial-gradient(ellipse 70% 30% at 55% 82%, var(--sky-glow) 0%, rgba(232,147,42,0) 100%),
      linear-gradient(180deg, var(--sky-top) 0%, var(--sky-mid) 45%, #d6882e 70%, #3a2417 88%, var(--rock) 100%);
  }
  .hero-rule {
    position: absolute;
    left: 49px;
    top: 0;
    width: 2px;
    height: 124px;
    background: var(--headline);
  }
  .headline {
    position: absolute;
    left: 63px;
    top: 62px;
    color: var(--headline);
    font-weight: 300;
    font-size: 27px;
    line-height: 34px;
  }
  .year {
    position: absolute;
    top: 480px;
    font-size: 88px;
    font-weight: 400;
    line-height: 1;
    color: transparent;
    -webkit-text-stroke: 1px var(--year-stroke);
    letter-spacing: 1px;
  }
  .year-old { left: 40px; }
  .year-new { left: 561px; }
</style>
</head>
<body>
  <main class="card">
    <header class="brand">
      <div class="brand-name"><span class="brand-dot"></span>Qorvella</div>
      <div class="brand-claim">DIENSTE FÜR MEHR WOHLGEFÜHL</div>
    </header>

    <section class="hero">
      <div class="hero-photo" role="img" aria-label="Silhouette einer Läuferin, die im Sonnenuntergang über eine Felsschlucht mit Fluss springt"></div>
      <div class="hero-rule"></div>
      <h1 class="headline">Das neue Jahr liegt<br>vor Ihnen.</h1>
      <span class="year year-old">2017</span>
      <span class="year year-new">2018</span>
    </section>
  </main>
</body>
</html>
```